The Brightwater Hour with Dale Morrow

Create Podcast Art for Podvale. My podcast is about overcoming adversities.

Everyone's adversity is different and there's no one-size-fits-all solution, but when you hear someone's else's story of resilience and add a little salt to it, you can find the inspiration you need to write a new ending to your struggle.

Maybe you're going through something right now and you're afraid:

● You won't be successful
● People are talking behind your back
● You'll never get the help you need
● You're not a good husband or wife
● Your child is out of control and you'll never get through to him or her
● There isn't a light at the end of your tunnel
● You'll never get your finances out of the red
● Your spouse won't ever see things your way
● The world is never gonna change

Every story we tell on The Brightwater Hour podcast challenges those thoughts, because everyday people going through everyday stuff just like you show us otherwise.

This podcast is for you. And, it's different.

Most interviews I do, I try to go on location and interview in person.

You might not see us together on the screen,
but you'll sense the raw sincerity and closeness of a side-by-side interview through your speakers.

The colors I have chosen below are close to the website colors. If you need a better view of that go here http://www.dalemorrowvoice.com

I've attached two pictures for the podcast. I'm not sure which one to use just yet so I put them both here to see what i created by your great people!

Target Market(s)

People who are currently going through an Advesirty or have been through one. 28 - 40 age group.

Colors
ec1f27
ffffff
000000
fbee3e

Requirements
Must have
• Eye appeal and The title "The Brightwater Hour" with Dale Morrow
• HAS to be stand-out, and it HAS to give a great first impression.
Nice to have
• The colors I have chosen are close to the website colors.

```html
<!DOCTYPE html>
<html lang="en">
<head>
<meta charset="utf-8">
<title>The Brightwater Hour with Dale Morrow — Podcast Art</title>
<link rel="stylesheet" href="https://fonts.googleapis.com/css2?family=Anton&family=Oswald:wght@600;700&display=swap">
<style>
  :root {
    --ink: #000000;
    --sun: #fbee3e;
    --signal: #ec1f27;
    --paper: #ffffff;
    --sweater-light: #9a9c9c;
    --sweater-dark: #4f5354;
    --brick-light: #d98a6a;
    --brick-dark: #8a3a28;
  }
  html, body {
    margin: 0;
    padding: 0;
    overflow: hidden;
    background: var(--ink);
  }
  .podcast-cover {
    position: relative;
    width: 1200px;
    height: 1200px;
    overflow: hidden;
    background: var(--ink);
  }
  .cover-shapes {
    position: absolute;
    inset: 0;
    width: 1200px;
    height: 1200px;
  }
  .show-title,
  .show-with,
  .host-name {
    position: absolute;
    margin: 0;
    transform: rotate(-18deg);
    transform-origin: left top;
    white-space: nowrap;
  }
  .show-title {
    left: 28px;
    top: 262px;
    font-family: "Oswald", sans-serif;
    font-weight: 600;
    font-size: 104px;
    line-height: 1;
    letter-spacing: -1px;
    color: var(--sun);
  }
  .show-with {
    left: 150px;
    top: 352px;
    font-family: "Oswald", sans-serif;
    font-weight: 700;
    font-size: 58px;
    line-height: 1;
    color: var(--paper);
  }
  .host-name {
    left: 98px;
    top: 628px;
    font-family: "Anton", sans-serif;
    font-size: 196px;
    line-height: 0.9;
    letter-spacing: -2px;
    color: var(--signal);
    text-transform: uppercase;
  }
  .host-name span { display: block; }
</style>
</head>
<body>
  <main class="podcast-cover">
    <svg class="cover-shapes" viewBox="0 0 1200 1200" xmlns="http://www.w3.org/2000/svg">
      <defs>
        <linearGradient id="host-tone" x1="0" y1="0" x2="1" y2="1">
          <stop offset="0" stop-color="var(--sweater-light)"/>
          <stop offset="1" stop-color="var(--sweater-dark)"/>
        </linearGradient>
        <linearGradient id="brick-tone" x1="0" y1="0" x2="1" y2="1">
          <stop offset="0" stop-color="var(--brick-light)"/>
          <stop offset="1" stop-color="var(--brick-dark)"/>
        </linearGradient>
      </defs>
      <polygon class="accent-band" points="0,515 1200,150 1200,570 0,915" fill="var(--sun)"/>
      <path class="brick-pile" role="img" aria-label="Photo of a pile of weathered red bricks"
            d="M0,990 L140,950 L300,960 L440,925 L600,895 L700,930 L720,1200 L0,1200 Z"
            fill="url(#brick-tone)"/>
      <path class="host-photo" role="img" aria-label="Photo of the host, seated and smiling, in a grey sweater over a checked shirt"
            d="M845,290 Q850,170 960,168 Q1075,172 1080,300 L1085,420 Q1160,450 1200,470 L1200,1200 L600,1200 L640,1010 L700,760 Q720,560 870,480 L860,420 Q835,380 845,290 Z"
            fill="url(#host-tone)"/>
    </svg>

    <h1 class="show-title">The Brightwater Hour</h1>
    <p class="show-with">with</p>
    <h2 class="host-name"><span>Dale</span><span>Morrow</span></h2>
  </main>
</body>
</html>
```